Metal Fabrication Business Cards

We need a business card for our business of Metal Fabrication/Welding. Our company is called "Hadley's Metal Fabrication"

We are a metal fabrication business which takes on "high class" clients- dealing with some of the biggest builders in Australia. Our work is neat, and the type of work we do is 2nd to none for quality. We want to show that on our cards. However, we would love to show a side that is down to earth and a bit more modern and contemporary - we are all young in business so would love to show that side - rather than a boring "very straight looking" card. We always have a clean workshop and take pride in our presentation. We want to come across like we are very rich, but would love to go for a surf as well! A card that basically says we have high class and will charge you a high rate - but the quality will be outstanding.

Front of card: - Simply but sharp!
-Thinking maybe white card - with nice black writing.
-On the right hand side of card a person welding - or holding a welder.
- My business name - Hadley's Metal Fabrication
-Also maybe my name - which is 'Corey" (if it doesn't work, we can put this on the back of card.)
- if needed to look better - we can put keywords on front of card like "metal fabrication, sheet metal, welding etc" but I dont want it to be crowded.

Back of card: - Also make smart but sharp!
Put details such as:
04387 21 914
hadley.fabrication@tinmailbox.com.au
7/32 Keel Street
East Tarrow NSW 2795
www.korvinfabrication.com.au
ABN 72 615 803 914

thats just an idea - its now up to you. I don't mind what you come up with - as long as it stands out from the rest and looks sharp, professional but contemporary.

Business

Put details such as:
04387 21 914
7/32 Keel Street
East Tarrow NSW 2795
ABN 72 615 803 914

Hadley's Metal Fabrication

```html
<!DOCTYPE html>
<html lang="en">
<head>
<meta charset="utf-8">
<title>Hadley's Metal Fabrication — Business Cards</title>
<link rel="stylesheet" href="https://fonts.googleapis.com/css2?family=Roboto:wght@400;700;900&display=swap">
<style>
  :root {
    --page: #ffffff;
    --card-black: #0b0b0b;
    --steel-dark: #8d8d8d;
    --steel-mid: #bdbdbd;
    --steel-light: #f4f4f4;
    --mark-grey: #3a3a3a;
    --mark-soft: #8a8a8a;
    --ink-white: #ffffff;
  }
  * { box-sizing: border-box; margin: 0; padding: 0; }
  html, body {
    width: 1200px;
    height: 1071px;
    overflow: hidden;
    background: var(--page);
    font-family: "Roboto", Arial, sans-serif;
  }
  .sheet {
    position: relative;
    width: 1200px;
    height: 1071px;
    display: flex;
    align-items: center;
    justify-content: center;
    gap: 40px;
  }
  .card {
    position: relative;
    width: 540px;
    height: 325px;
    background: var(--card-black);
    overflow: hidden;
  }
  .steel-band {
    position: absolute;
    left: 0;
    width: 100%;
    background: linear-gradient(90deg,
      var(--steel-dark) 0%, var(--steel-light) 12%, var(--steel-mid) 26%,
      var(--steel-light) 40%, var(--steel-dark) 52%, var(--steel-light) 66%,
      var(--steel-mid) 80%, var(--steel-light) 90%, var(--steel-dark) 100%);
  }

  /* Front */
  .card-front .steel-band { top: 152px; height: 60px; }
  .front-brand {
    position: absolute;
    left: 0; right: 0;
    top: 70px;
    display: flex;
    flex-direction: column;
    align-items: center;
  }
  .front-brand .brand-dot {
    width: 58px; height: 58px;
    border-radius: 50%;
    background: var(--mark-soft);
    margin-bottom: 24px;
  }
  .front-brand .brand-name {
    font-weight: 900;
    color: var(--mark-grey);
    font-size: 24px;
    line-height: 26px;
    letter-spacing: 1.5px;
    text-align: center;
    text-transform: uppercase;
  }

  /* Back */
  .card-back .steel-band { top: 0; height: 92px; }
  .back-brand {
    position: absolute;
    top: 24px;
    left: 215px;
    width: 190px;
    display: flex;
    flex-direction: column;
    align-items: center;
    gap: 4px;
  }
  .back-brand .brand-dot {
    width: 26px; height: 26px;
    border-radius: 50%;
    background: var(--mark-grey);
  }
  .back-brand .brand-name {
    font-weight: 900;
    color: var(--mark-grey);
    font-size: 11px;
    line-height: 12px;
    letter-spacing: 1px;
    text-transform: uppercase;
    text-align: center;
  }
  .person {
    position: absolute;
    left: 50px;
    top: 185px;
    color: var(--ink-white);
    text-align: center;
  }
  .person .name {
    font-weight: 900;
    font-size: 29px;
    line-height: 30px;
    text-transform: uppercase;
    letter-spacing: 0.5px;
  }
  .person .role {
    font-weight: 700;
    font-size: 11px;
    letter-spacing: 0.5px;
    text-transform: uppercase;
  }
  .contact-list {
    position: absolute;
    left: 218px;
    top: 162px;
    list-style: none;
    color: var(--ink-white);
    font-weight: 700;
    font-size: 13px;
    line-height: 16px;
  }
  .contact-list li {
    display: flex;
    align-items: flex-start;
    gap: 12px;
    margin-bottom: 10px;
  }
  .contact-list svg {
    flex: 0 0 14px;
    width: 14px; height: 14px;
    margin-top: 1px;
    fill: var(--ink-white);
  }
  .contact-list .email { font-size: 12.5px; }
</style>
</head>
<body>
<main class="sheet">
  <section class="card card-front" aria-label="Business card front">
    <div class="steel-band"></div>
    <div class="front-brand">
      <span class="brand-dot"></span>
      <p class="brand-name">Hadley's Metal<br>Fabrication</p>
    </div>
  </section>

  <section class="card card-back" aria-label="Business card back">
    <div class="steel-band"></div>
    <div class="back-brand">
      <span class="brand-dot"></span>
      <p class="brand-name">Hadley's Metal<br>Fabrication</p>
    </div>
    <div class="person">
      <p class="name">Corey</p>
      <p class="role">Director</p>
    </div>
    <ul class="contact-list">
      <li>
        <svg viewBox="0 0 14 14" aria-hidden="true"><path d="M3 0h6a1.5 1.5 0 0 1 1.5 1.5v11A1.5 1.5 0 0 1 9 14H3a1.5 1.5 0 0 1-1.5-1.5v-11A1.5 1.5 0 0 1 3 0zm.5 2v8h5V2zM6 11a.9.9 0 1 0 0 1.8A.9.9 0 0 0 6 11z"/></svg>
        <span>04387 21 914</span>
      </li>
      <li>
        <svg viewBox="0 0 14 14" aria-hidden="true"><path d="M0 3h14v8.5H0zm1.4 1.2L7 8l5.6-3.8V3.9L7 7.4 1.4 3.9z"/></svg>
        <span class="email">hadley.fabrication@tinmailbox.com.au</span>
      </li>
      <li>
        <svg viewBox="0 0 14 14" aria-hidden="true"><path fill-rule="evenodd" d="M7 0a7 7 0 1 1 0 14A7 7 0 0 1 7 0zm0 1.2A5.8 5.8 0 1 0 7 12.8 5.8 5.8 0 0 0 7 1.2zM6.4 1.5h1.2v11H6.4zM1.5 6.4h11v1.2h-11zM2.5 3.6h9v1h-9zm0 5.8h9v1h-9z"/></svg>
        <span>www.korvinfabrication.com.au</span>
      </li>
      <li>
        <svg viewBox="0 0 14 14" aria-hidden="true"><path d="M7 1l7 6h-2v6H8.5V9h-3v4H2V7H0z"/></svg>
        <span>7/32 Keel Street East Tarrow<br>NSW 2795</span>
      </li>
    </ul>
  </section>
</main>
</body>
</html>
```